Indian Lunch Delivery company needs a google ad banner for advertising its offering

We are a Kolkata, India based startup delivering lunch to office buildings in the city. We only serve set meals (vegetarian and non-vegetarian). Minimum order quantity is 5 boxes. The name of the brand is Brimvora (Thali=platter). Our USP-
We cook fresh
Trans-fat free
No emulsifiers, preservatives or artificial colorings used.
Importantly, we are a value for money brand. To be precise our meals costs just .99 c.
Target Market(s)
Young professionals
Industry/Entity Type
It Company
Font styles to use
Sans Serif
Requirements
Must have
- Home made food feel to it
Nice to have
- Lots of colours

```html
<!DOCTYPE html>
<html lang="en">
<head>
<meta charset="utf-8">
<title>Brimvora – Fresh Set Meals</title>
<link rel="stylesheet" href="https://fonts.googleapis.com/css2?family=Roboto:wght@400;500;700&display=swap">
<style>
  :root {
    --bg-purple: #5a1c6f;
    --text-orange: #ea7a3c;
    --text-yellow: #f3d22f;
    --meal-orange: #f0a03a;
    --meal-brown: #8a5a35;
  }
  html, body {
    margin: 0;
    padding: 0;
    overflow: hidden;
    background: var(--bg-purple);
  }
  .banner {
    position: relative;
    width: 1200px;
    height: 232px;
    background: var(--bg-purple);
    font-family: "Roboto", Arial, sans-serif;
    overflow: hidden;
  }
  .banner__meal-art {
    position: absolute;
    left: 64px;
    top: 40px;
    width: 142px;
    height: 120px;
    border-radius: 18px;
    background: linear-gradient(160deg, var(--meal-orange) 0%, #c9762f 55%, var(--meal-brown) 100%);
  }
  .banner__line {
    position: absolute;
    margin: 0;
    line-height: 1;
    white-space: nowrap;
  }
  .usp {
    left: 287px;
    color: var(--text-orange);
    font-weight: 400;
  }
  .usp--fresh { top: 49px; font-size: 31px; }
  .usp--transfat { top: 93px; font-size: 31px; }
  .usp--clean { top: 126px; font-size: 21px; }
  .price {
    left: 290px;
    top: 167px;
    font-size: 46px;
    font-weight: 500;
    color: var(--text-yellow);
  }
  .brand-name {
    right: 52px;
    top: 40px;
    font-size: 78px;
    font-weight: 700;
    color: var(--text-yellow);
  }
  .footnote {
    right: 8px;
    top: 213px;
    font-size: 15px;
    color: var(--text-orange);
  }
</style>
</head>
<body>
  <div class="banner">
    <div class="banner__meal-art" role="img" aria-label="Illustration of a homemade meal platter with a flame and a red chili"></div>

    <p class="banner__line usp usp--fresh">We cook fresh</p>
    <p class="banner__line usp usp--transfat">Trans-fat free</p>
    <p class="banner__line usp usp--clean">No emulsifiers, preservatives or artificial colorings used.</p>

    <p class="banner__line price">Our meals costs just .99c only.</p>

    <h1 class="banner__line brand-name">Brimvora</h1>

    <p class="banner__line footnote">*Only serve set meals</p>
  </div>
</body>
</html>
```